Tamsel Loans - Mortgage Brokers Australia

redesign of tamselloans.com.au website. We are a mortgage brokering service and are clients are based in Australia. The demographics are 30-45 year holds looking to borrow money to purchase, invest and refinance property.

Please research other lending websites in Australia. My favourites are:

https://www.korvu.com.au/
https://www.brivanest.com.au/

I want CTA's on the first page. For Refinance/Purchase.

I DO NOT WANT ANYONE TO TRY AND CONTACT ME VIA EMAIL/What's app

My current website is: https/www.tamselloans.com.au/home and the password is "Rbqw8175?"

Target Market(s)

30-45 year hold professionals, first home buyers

Industry/Entity Type

Mortgage Brokerage

Number of Pages Required

4 page

Font styles to use
Sans Serif

Colors
e34197
6b449b
ffc214
0792cd
34a7d8

Requirements
Must have
• Must be fresh, clean and professional - with a beautiful hero section

```html
<!DOCTYPE html>
<html lang="en">
<head>
<meta charset="utf-8">
<title>Tamsel Loans – Mortgage Brokers Australia</title>
<link href="https://fonts.googleapis.com/css2?family=Raleway:wght@300;400;500;600;700;800;900&display=swap" rel="stylesheet">
<style>
:root{
  --purple:#4e2f6b;
  --purple-deep:#3b2454;
  --pink:#e34197;
  --yellow:#f2b705;
  --ink:#2b2b2b;
  --grey:#7d7d7d;
  --light:#f3f3f3;
  --footer:#232323;
  --white:#fff;
}
*{box-sizing:border-box;margin:0;padding:0}
html,body{width:1200px;height:3566px;overflow:hidden}
body{position:relative;font-family:"Raleway",sans-serif;color:var(--ink);background:var(--white)}
.abs{position:absolute}
.btn{position:absolute;display:flex;align-items:center;justify-content:center;background:var(--purple);color:#fff;font-weight:800;font-size:13px;text-decoration:none}
.eyebrow{font-size:16px;color:var(--yellow);font-weight:500;text-transform:uppercase}
.heading{font-weight:900;font-size:44px;line-height:48px;color:var(--ink);text-transform:uppercase;letter-spacing:-.5px}
.photo{position:absolute}

/* header */
.topbar{left:910px;top:0;width:290px;height:40px;background:var(--purple);border-bottom-left-radius:30px;color:#fff;font-size:14px;font-weight:700;display:flex;align-items:center;padding-left:45px;gap:6px}
.brand{left:112px;top:50px;display:flex;align-items:center;gap:8px;font-size:30px;font-weight:700;color:var(--pink)}
.brand .dot{width:22px;height:22px;background:var(--yellow);border-radius:50%}
.nav{right:112px;top:66px;display:flex;gap:41px;font-size:12px;font-weight:500;color:#444}
.nav .active{color:var(--pink)}

/* hero */
.hero{left:0;top:105px;width:1200px;height:598px;
  background:linear-gradient(90deg,#e9ecee 0%,#dfe3e4 6%,#c9d3c6 11%,#8fa58a 15%,#c6d0c2 19%,#e4e7e9 25%,#d6d0c7 33%,#c9cfd8 40%,#f1f3f5 46%,#dfe6ee 52%,#cfd8e3 57%,#eef1f4 64%,#f8f9fa 76%,#fbfcfc 100%)}
.hero-wedge{left:0;top:105px}
.hero-copy{left:743px;top:290px}
.hero-copy .eyebrow{font-size:18px}
.hero-copy h1{font-weight:900;font-size:44px;line-height:45px;margin-top:10px;color:#222}
.hero-copy p{font-size:22px;font-weight:500;margin-top:12px}
.hero-btn{font-size:12px;font-weight:600}
.loan-bar{left:113px;top:615px;width:607px;height:88px;background:rgba(30,30,36,.88);display:flex;align-items:center;justify-content:space-around;padding:0 14px;color:#fff;font-size:13px;font-weight:500}
.loan-bar span{display:flex;align-items:center;gap:8px}
.loan-bar i{width:22px;height:22px;border-radius:4px;background:var(--yellow);display:inline-block}
.slider-dots{left:53px;top:390px;width:6px;height:26px;background:linear-gradient(var(--yellow) 0 6px,transparent 6px 10px,#fff 10px 16px,transparent 16px 20px,#fff 20px)}

/* work */
.body-text{font-size:14.5px;line-height:23.5px;color:var(--grey);font-weight:400}

/* checklist */
.checks{list-style:none;font-size:13.5px;color:#555}
.checks li{height:35.3px;display:flex;align-items:center;gap:9px}

/* services / blog cards */
.card-title{font-size:18px;font-weight:600;color:#222;line-height:24px}
.card-text{font-size:13.5px;line-height:20px;color:var(--grey)}

/* cta */
.cta{left:0;top:2198px;width:1200px;height:360px;background:linear-gradient(180deg,#2a3a55 0%,#3c4b63 55%,#2c3b2e 100%);color:#fff;text-align:center}
.partners{left:0;top:2558px;width:1200px;height:94px;background:var(--light);display:flex;justify-content:space-around;align-items:center;padding:0 110px}
.partner{font-size:24px;font-weight:800;color:var(--purple);display:flex;align-items:center;gap:8px}
.partner i{width:26px;height:26px;border-radius:50%;background:var(--yellow);display:inline-block}

/* footer */
.footer{left:0;top:3247px;width:1200px;height:319px;background:var(--footer);color:#ddd}
.footer h4{font-size:15px;font-weight:600;color:#fff;margin-bottom:14px}
.footer li{list-style:none;font-size:12px;line-height:26px;color:#cfcfcf}
.footer .about{font-size:12px;line-height:18px;color:#cfcfcf;width:260px}
.social li{display:flex;align-items:center;gap:8px;height:35px}
.social i{width:30px;height:30px;background:#2c6fb7;border-radius:4px;display:inline-block}
.contact li{display:flex;gap:8px;line-height:16px;margin-bottom:22px}
.copyright{left:0;top:3505px;width:1200px;text-align:center;font-size:10px;color:#bbb}
.copyright b{color:var(--yellow);font-weight:500}
</style>
</head>
<body>

<div class="abs topbar">
  <svg width="14" height="18" viewBox="0 0 14 18"><path d="M3 1l3 4-2 2c1 3 3 5 5 6l2-2 3 3-2 3C6 16 1 10 1 3z" fill="var(--yellow)"/></svg>
  (02) 7412 3068
</div>
<div class="abs brand"><span class="dot"></span>Tamsel Loans</div>
<nav class="abs nav">
  <span class="active">HOME</span><span>OUR SERVICES</span><span>ABOUT US</span><span>WHY USE BROKER</span><span>BLOG</span><span>CONTACT US</span>
</nav>

<div class="abs hero" role="img" aria-label="Smiling broker in a white shirt and blue tie holding a small model house in a bright office with a shelf and potted plant"></div>
<svg class="abs hero-wedge" width="1200" height="598" viewBox="0 0 1200 598">
  <path d="M700 598 C880 560 1060 520 1200 470 L1200 598 Z" fill="#ffffff" opacity=".75"/>
  <path d="M1140 0 C1170 120 1190 250 1200 330 L1200 0 Z" fill="#cfe0e4" opacity=".6"/>
</svg>
<div class="abs slider-dots"></div>
<div class="abs hero-copy">
  <div class="eyebrow">We are</div>
  <h1>PASSIONATE<br>ABOUT ACHIEVE</h1>
  <p>Your Financial Goals!</p>
</div>
<a class="btn hero-btn" style="left:742px;top:466px;width:167px;height:47px">I WANT TO BUY A HOME</a>
<a class="btn hero-btn" style="left:922px;top:466px;width:166px;height:47px;background:var(--pink)">I WANT TO REFINANCE</a>
<div class="abs loan-bar">
  <span><i></i>HOME LOAN</span><span><i></i>PERSONAL LOAN</span><span><i></i>CAR LOAN</span><span><i></i>INVESTMENT LOAN</span>
</div>

<div class="abs eyebrow" style="left:112px;top:776px">Our Work</div>
<h2 class="abs heading" style="left:112px;top:806px">How we work<br>with you</h2>
<p class="abs body-text" style="left:112px;top:923px;width:548px">Tamsel Loans manage the entire process for you from start to finish and as every one of our clients is different, we fully assess your individual situation and provide a solution to meet your particular needs. Quite simply, we do everything necessary to get you the best possible rate and importantly get your loan over the line. You don't do anything except allow us to act on your behalf.</p>
<a class="btn" style="left:112px;top:1066px;width:134px;height:48px">READ MORE</a>
<div class="photo" style="left:696px;top:757px;width:392px;height:381px;border-bottom-right-radius:60px;background:linear-gradient(135deg,#cfc3b4,#8a8f96 60%,#3a3d44)" role="img" aria-label="Couple meeting a broker at a desk"></div>

<svg class="abs" style="left:111px;top:1190px" width="433" height="422" viewBox="0 0 433 422" role="img" aria-label="Broker in a suit holding a model house while colleagues review plans">
  <defs><linearGradient id="blobFill" x1="0" y1="0" x2="1" y2="1"><stop offset="0" stop-color="#e7e5e2"/><stop offset="1" stop-color="#7d8a9a"/></linearGradient></defs>
  <path d="M200 2C300 -6 420 60 432 190 440 300 380 410 250 420 130 428 30 380 8 280 -12 170 70 10 200 2z" fill="url(#blobFill)"/>
</svg>
<div class="abs eyebrow" style="left:612px;top:1198px">Features</div>
<h2 class="abs heading" style="left:612px;top:1229px">We assess &amp; tailor<br>your mortgage</h2>
<div class="abs" style="left:612px;top:1325px;font-size:18px;font-weight:500;color:#444">TO SUIT YOUR FINANCIAL SITUATION</div>
<ul class="abs checks" style="left:612px;top:1363px">
  <li><svg width="14" height="12" viewBox="0 0 14 12"><path d="M1 6l4 4 8-9" stroke="var(--purple)" stroke-width="2.5" fill="none"/></svg>We listen to you and learn</li>
  <li><svg width="14" height="12" viewBox="0 0 14 12"><path d="M1 6l4 4 8-9" stroke="var(--purple)" stroke-width="2.5" fill="none"/></svg>We create breathing space for you</li>
  <li><svg width="14" height="12" viewBox="0 0 14 12"><path d="M1 6l4 4 8-9" stroke="var(--purple)" stroke-width="2.5" fill="none"/></svg>We develop your Mortgage plan</li>
  <li><svg width="14" height="12" viewBox="0 0 14 12"><path d="M1 6l4 4 8-9" stroke="var(--purple)" stroke-width="2.5" fill="none"/></svg>We select the right financial institution</li>
  <li><svg width="14" height="12" viewBox="0 0 14 12"><path d="M1 6l4 4 8-9" stroke="var(--purple)" stroke-width="2.5" fill="none"/></svg>We help build your secure future</li>
</ul>
<a class="btn" style="left:612px;top:1557px;width:134px;height:47px">READ MORE</a>

<div class="abs eyebrow" style="left:0;top:1688px;width:1200px;text-align:center">What can</div>
<h2 class="abs heading" style="left:0;top:1716px;width:1200px;text-align:center">Tamsel Loans do for you?</h2>

<div class="photo" style="left:112px;top:1787px;width:307px;height:188px;background:linear-gradient(135deg,#9aa3ad,#e6e2dc)" role="img" aria-label="Broker presenting a model house to a couple"></div>
<div class="abs card-title" style="left:111px;top:1990px">HOME LOANS</div>
<p class="abs card-text" style="left:112px;top:2022px;width:290px">Your home loan is likely to be one of your life's biggest...</p>
<a class="btn" style="left:110px;top:2076px;width:107px;height:43px">READ MORE</a>

<div class="photo" style="left:446px;top:1787px;width:307px;height:188px;background:linear-gradient(135deg,#c9ccd2,#f3f2f0)" role="img" aria-label="Couple reviewing a laptop with an adviser"></div>
<div class="abs card-title" style="left:447px;top:1990px">REFINANCE</div>
<p class="abs card-text" style="left:447px;top:2022px;width:290px">Refinancing refers to the process of paying out your current...</p>
<a class="btn" style="left:446px;top:2076px;width:108px;height:43px">READ MORE</a>

<div class="photo" style="left:781px;top:1787px;width:307px;height:188px;background:linear-gradient(135deg,#d4d2cd,#8c8f95)" role="img" aria-label="Adviser discussing charts with a client"></div>
<div class="abs card-title" style="left:781px;top:1990px">INVESTMENT LOANS</div>
<p class="abs card-text" style="left:783px;top:2022px;width:290px">Would you like to make your money work for you? Use...</p>
<a class="btn" style="left:780px;top:2076px;width:108px;height:43px">READ MORE</a>

<div class="abs cta" role="img" aria-label="Evening city skyline with a tall iron tower"></div>
<div class="abs" style="left:0;top:2277px;width:1200px;text-align:center;color:#fff">
  <div style="font-size:25px;font-weight:500">GIVE US A CHANCE</div>
  <div style="font-size:46px;font-weight:900;line-height:52px">TO MAKE A DIFFERENCE!</div>
  <p style="font-size:14.5px;line-height:22px;margin-top:12px">We're all about helping you reach your next financial goal—great rates, less fees, unprecedented service,<br>and awesome loan help.</p>
</div>
<a class="btn" style="left:530px;top:2428px;width:137px;height:45px;background:var(--pink)">BOOK NOW</a>

<div class="abs partners">
  <span class="partner"><i></i>CORVALE</span>
  <span class="partner">MERIDAN</span>
  <span class="partner">THISTLE</span>
  <span class="partner">ORVENBANK</span>
</div>

<h2 class="abs heading" style="left:0;top:2722px;width:1200px;text-align:center">Latest blog</h2>

<div class="photo" style="left:112px;top:2783px;width:307px;height:194px;background:linear-gradient(180deg,#9fc3e2,#c9a27a)" role="img" aria-label="Dog looking out a car window across a desert road"></div>
<div class="abs card-title" style="left:111px;top:2989px;width:300px">Flow of credit to small businesses remains strong</div>
<p class="abs card-text" style="left:112px;top:3047px;width:300px;font-size:12px;line-height:21px">Small business owners in need of credit will be buoyed by new data that shows the approval rate for loans has remained strong...</p>
<a class="btn" style="left:111px;top:3125px;width:108px;height:43px">READ MORE</a>

<div class="photo" style="left:446px;top:2783px;width:307px;height:194px;background:linear-gradient(135deg,#3d4f7a,#8d97b3)" role="img" aria-label="Man whispering news to a surprised woman"></div>
<div class="abs card-title" style="left:446px;top:2989px;width:300px">WorkBridge 2.0 is about to begin: here's what you need to know</div>
<p class="abs card-text" style="left:446px;top:3047px;width:300px;font-size:12px;line-height:21px">Like most sequels, WorkBridge 2.0 won't be as big a blockbuster as the original. But that's not to say it won't help many...</p>
<a class="btn" style="left:446px;top:3125px;width:108px;height:43px">READ MORE</a>

<div class="photo" style="left:781px;top:2783px;width:307px;height:194px;background:linear-gradient(135deg,#b9c3b0,#efe6d6)" role="img" aria-label="Parent with a child at a laptop in a bright kitchen"></div>
<div class="abs card-title" style="left:780px;top:2989px;width:310px">Is now a good time to buy property? Two-thirds of investors say 'yes'</div>
<p class="abs card-text" style="left:780px;top:3047px;width:305px;font-size:12px;line-height:21px">The majority of property investors are remaining upbeat despite COVID-19, with 67% believing now is a good time to invest in residential property...</p>
<a class="btn" style="left:780px;top:3125px;width:108px;height:43px">READ MORE</a>

<footer class="abs footer">
  <div class="abs" style="left:112px;top:46px">
    <h4>ABOUT US</h4>
    <p class="about">It is far too often that you hear of people ending up with the wrong type of loan, a bad deal, or sign up with promises that are never kept.</p>
    <div style="margin-top:40px;font-size:20px;font-weight:700;color:var(--pink)">Tamsel Loans</div>
  </div>
  <div class="abs" style="left:421px;top:46px">
    <h4>SITEMAP</h4>
    <ul><li>Home</li><li>Our Services</li><li>About Us</li><li>Why Use Broker</li><li>Blog</li><li>Contact Us</li></ul>
  </div>
  <div class="abs" style="left:584px;top:46px">
    <h4>SERVICES</h4>
    <ul><li>Home Loan</li><li>Refinance</li><li>Investment Loan</li><li>Car Loan</li><li>Personal Loan</li></ul>
  </div>
  <div class="abs contact" style="left:739px;top:46px">
    <h4>CONTACT US</h4>
    <ul>
      <li><svg width="10" height="14" viewBox="0 0 10 14"><path d="M5 0a5 5 0 0 1 5 5c0 4-5 9-5 9S0 9 0 5a5 5 0 0 1 5-5z" fill="var(--yellow)"/></svg><span>24 Larkspur Lane Glenhaven,<br>NSW 2156 Australia</span></li>
      <li><svg width="10" height="14" viewBox="0 0 14 18"><path d="M3 1l3 4-2 2c1 3 3 5 5 6l2-2 3 3-2 3C6 16 1 10 1 3z" fill="var(--yellow)"/></svg><span>0431 806 219</span></li>
      <li><svg width="12" height="10" viewBox="0 0 12 10"><rect width="12" height="10" fill="var(--yellow)"/><path d="M0 0l6 5 6-5" stroke="#232323" fill="none"/></svg><span>info@tamselloans.com.au</span></li>
    </ul>
  </div>
  <div class="abs social" style="left:987px;top:46px">
    <h4>SOCIAL ON</h4>
    <ul><li><i></i>Community</li><li><i></i>Updates</li><li><i></i>Network</li><li><i></i>Gallery</li></ul>
  </div>
</footer>
<div class="abs copyright">COPYRIGHT © 2021 <b>TAMSEL LOANS</b>. ALL RIGHTS RESERVED.</div>

</body>
</html>
```